DRIFTWATER a novel

He loves her, she loves him, and they work in a bar in Covent Garden. He is American; she is British. Brexit has happened and they don't care. His wife has called from America (ex-wife) and they don't care. They don't care about much because they are in their bar, and their bar is their haven. Sometimes it's Pelican Noir in there; sometimes it's the blues. They don't care. They are just a bit toooo cool, calm and collected. Let's send some wind up their sails.

Driftwater is the first in a three-part story about a man and a woman who love each other because life is simple. Music is important in the series, and music of the 70s, 80s and 90s. The covers have to capture their cool, easy way, and yet say "this is a love story". The books brings them their romance.

Author is Marnie Fenwick.

Image ideas: a Covent Garden setting for literal. A mermaid for symbolic. A music note for metaphorical. A lily for beauty.

```html
<!DOCTYPE html>
<html lang="en">
<head>
<meta charset="utf-8">
<title>Driftwater — a novel by Marnie Fenwick</title>
<link rel="stylesheet" href="https://fonts.googleapis.com/css2?family=Pathway+Gothic+One&display=swap">
<style>
  :root {
    --backdrop: #ececec;
    --cover-black: #000000;
    --type-white: #f2f2f2;
    --lily-violet: #9b5fe0;
    --lily-pink: #c98cf0;
    --lily-glow: #f4e9ff;
    --lily-shadow: #2a1240;
  }
  html, body {
    margin: 0;
    padding: 0;
    width: 1200px;
    height: 800px;
    overflow: hidden;
    background: var(--backdrop);
  }
  .canvas {
    position: relative;
    width: 1200px;
    height: 800px;
  }
  .book-cover {
    position: absolute;
    left: 358px;
    top: 30px;
    width: 484px;
    height: 740px;
    background: var(--cover-black);
    border-radius: 3px;
    overflow: hidden;
    font-family: "Pathway Gothic One", "Arial Narrow", sans-serif;
    color: var(--type-white);
    text-align: center;
  }
  .author-name {
    position: absolute;
    top: 50px;
    left: 0;
    right: 0;
    margin: 0;
    font-size: 38px;
    font-weight: 400;
    letter-spacing: 4px;
  }
  .book-title {
    position: absolute;
    top: 186px;
    left: 0;
    right: 0;
    margin: 0;
    font-size: 66px;
    font-weight: 400;
    letter-spacing: 8px;
  }
  .book-subtitle {
    position: absolute;
    top: 300px;
    left: 0;
    right: 0;
    margin: 0;
    font-size: 38px;
    letter-spacing: 5px;
  }
  .lily-artwork {
    position: absolute;
    left: 0;
    right: 0;
    bottom: 0;
    height: 350px;
    background:
      radial-gradient(ellipse 8% 6% at 50% 86%, var(--lily-glow) 0%, transparent 100%),
      radial-gradient(ellipse 60% 30% at 50% 82%, var(--lily-pink) 0%, var(--lily-violet) 45%, transparent 100%),
      radial-gradient(ellipse 18% 40% at 52% 40%, var(--lily-shadow) 0%, transparent 100%),
      var(--cover-black);
  }
</style>
</head>
<body>
  <main class="canvas">
    <article class="book-cover">
      <p class="author-name">Marnie Fenwick</p>
      <h1 class="book-title">DRIFTWATER</h1>
      <p class="book-subtitle">a novel</p>
      <div class="lily-artwork" role="img" aria-label="Photograph of a glowing violet water lily with a swirl of purple sparkles rising from its centre"></div>
    </article>
  </main>
</body>
</html>
```